Simple and Approachable Cover for Pet Expo Company Page

Size: 2000 x 430; looking simply for words "Tenbury HR Consulting" and email address "TenburyHRConsulting@mailvane.com." This is for a cover photo for a company profile page for the Northway Animal Fair, where I am a featured speaker on Employee Communications later this month. You can incorporate the attached photo to the left of the banner ad if you wish. The mood I wish to present is approachable, positive and simple.

Target Market(s)

small pet retail business owners

Industry/Entity Type

Pet Shop

Font styles to use
Serif
Sans Serif

Requirements
Must have
• Email address clearly defined/separated. Easy to read.
Nice to have
• I like the picture that I included; subtle pet paw background is also nice
Should not have
• No paid stock images

```html
<!DOCTYPE html>
<html lang="en">
<head>
<meta charset="utf-8">
<title>Tenbury HR Consulting – Cover Banner</title>
<link rel="stylesheet" href="https://fonts.googleapis.com/css2?family=Rubik:wght@500;600;700&display=swap">
<style>
  :root {
    --page-bg: #676767;
    --navy: #0b4a8c;
    --navy-deep: #073a73;
    --navy-light: #1a5b9e;
    --gold: #f5cb3a;
    --orange: #ec8a1f;
    --white: #ffffff;
    --photo-sky: #6f7a4e;
    --photo-grass: #7f8f47;
    --photo-earth: #a08a62;
  }
  * { margin: 0; padding: 0; box-sizing: border-box; }
  html, body {
    width: 1200px;
    height: 1000px;
    overflow: hidden;
    background: var(--page-bg);
  }
  .cover-banner {
    position: absolute;
    left: 54px;
    top: 341px;
    width: 1082px;
    height: 232px;
    overflow: hidden;
    background: linear-gradient(100deg, var(--navy-light) 0%, var(--navy) 45%, var(--navy-deep) 100%);
    font-family: "Rubik", Arial, sans-serif;
  }
  .banner-layer {
    position: absolute;
    inset: 0;
    width: 1082px;
    height: 232px;
  }
  .brand-block {
    position: absolute;
    left: 0;
    top: 0;
    width: 532px;
    height: 232px;
    text-align: center;
    color: var(--white);
  }
  .brand-name-top {
    position: absolute;
    left: 0;
    right: 0;
    top: 27px;
    font-size: 50px;
    font-weight: 500;
    letter-spacing: 0.5px;
    line-height: 1;
  }
  .brand-name-main {
    position: absolute;
    left: 0;
    right: 0;
    top: 80px;
    font-size: 66px;
    font-weight: 600;
    color: var(--gold);
    letter-spacing: 1px;
    line-height: 1;
  }
  .brand-rule {
    position: absolute;
    left: 197px;
    top: 155px;
    width: 140px;
    height: 3px;
    background: var(--orange);
  }
  .contact-email {
    position: absolute;
    left: 0;
    right: 0;
    top: 172px;
    font-size: 24px;
    font-weight: 500;
    line-height: 1.2;
    white-space: nowrap;
  }
</style>
</head>
<body>
  <div class="cover-banner">
    <svg class="banner-layer speaker-photo" role="img" aria-label="Photo of the consultants sitting on the grass with their two hound dogs under large oak trees" viewBox="0 0 1082 232">
      <defs>
        <linearGradient id="photoTone" x1="0" y1="0" x2="0" y2="1">
          <stop offset="0" stop-color="var(--photo-sky)"/>
          <stop offset="0.45" stop-color="var(--photo-earth)"/>
          <stop offset="1" stop-color="var(--photo-grass)"/>
        </linearGradient>
      </defs>
      <path d="M555,0 L1082,0 L1082,232 L660,232 C610,170 570,90 555,0 Z" fill="url(#photoTone)"/>
    </svg>

    <svg class="banner-layer swoosh-accents" aria-hidden="true" viewBox="0 0 1082 232">
      <path class="swoosh-gold" d="M478,0 L522,0 C540,90 585,170 642,232 L620,232 C560,160 505,80 478,0 Z" fill="var(--gold)"/>
      <path class="swoosh-white" d="M520,0 L558,0 C572,90 612,170 662,232 L640,232 C585,170 540,90 520,0 Z" fill="var(--white)"/>
      <path class="corner-gold" d="M942,0 L1082,0 L1082,74 C1028,66 972,42 942,0 Z" fill="var(--gold)"/>
      <path class="corner-navy" d="M975,0 L1082,0 L1082,66 C1040,58 1000,36 975,0 Z" fill="var(--navy)"/>
    </svg>

    <div class="brand-block">
      <div class="brand-name-top">TENBURY HR</div>
      <div class="brand-name-main">CONSULTING</div>
      <div class="brand-rule"></div>
      <div class="contact-email">TenburyHRConsulting@mailvane.com.</div>
    </div>
  </div>
</body>
</html>
```